Webpage Needed for Bright Harbor Wiring Electrical and Security

We need a web design for our company showing people we arent just a small business. We want to look big so people can trust us. I would like information from my business cards on the page. example, we do all house rennovations, construction, commercial, 24 hour emergency service, new installations, repairs, maintenance, home theatre and so on...

I would also like images from my facebook on the page and linked. facebook.com/brightharborwiring

Target Market(s)

builders, residents,

Industry/Entity Type

Business

Number of Pages Required

1 page

Font styles to use
Other font styles liked:
• Juice bold

Requirements
Must have
• colours the same as the logo. background must be white. also the font must be Juice Bold which is the font of the logo
Should not have
• black as the background

```html
<!DOCTYPE html>
<html lang="en">
<head>
<meta charset="utf-8">
<title>Bright Harbor Wiring – Electrical and Security</title>
<link href="https://fonts.googleapis.com/css2?family=Raleway:wght@400;500;600&family=Open+Sans:ital,wght@0,400;0,600;1,400&display=swap" rel="stylesheet">
<style>
:root{
  --orange:#ef7a4a;
  --orange-deep:#e9622d;
  --blue:#2e9fe0;
  --blue-dark:#1a86c8;
  --ink:#222a33;
  --text:#5b5f66;
  --muted:#8a8e94;
  --line:#d9dcdf;
  --footer:#efefef;
  --white:#ffffff;
}
*{margin:0;padding:0;box-sizing:border-box}
html,body{width:1074px;height:1200px;overflow:hidden;background:var(--white)}
body{position:relative;font-family:'Open Sans',Arial,sans-serif;color:var(--text)}
.abs{position:absolute}

/* header */
.brand{left:136px;top:34px;width:240px;font-family:'Raleway',Arial,sans-serif;font-weight:600;color:var(--ink);line-height:1.15}
.brand-name{font-size:22px;display:block}
.brand-sub{font-size:14px;display:block;margin-top:4px}
.enquiry{right:138px;top:76px;text-align:right}
.enquiry-label{color:var(--orange);font-size:17px;display:block}
.enquiry-phone{color:var(--ink);font-size:22px;display:flex;align-items:center;gap:5px;margin-top:2px}

/* nav */
.main-nav{left:0;top:136px;width:1074px;height:48px;background:linear-gradient(#67c8f3,#2b9ee0)}
.main-nav a{position:absolute;top:0;height:48px;line-height:48px;color:var(--white);text-decoration:none;font-family:'Raleway',Arial,sans-serif;font-weight:500;font-size:14.5px;transform:translateX(-50%);white-space:nowrap}
.nav-sep{position:absolute;top:0;width:1px;height:48px;background:rgba(255,255,255,.45)}

/* hero */
.hero{left:0;top:184px;width:1074px;height:426px;background:linear-gradient(100deg,#6e6459 0%,#4a4a4a 35%,#8c8c88 55%,#e6e8ea 75%,#cfd3d6 100%)}
.hero-title{left:133px;top:338px;width:323px;height:52px;background:var(--orange-deep);clip-path:polygon(0 0,96% 0,100% 100%,0 100%);color:var(--white);font-family:'Raleway',Arial,sans-serif;font-size:29px;line-height:52px;padding-left:21px}
.hero-sub{left:133px;top:390px;width:420px;height:52px;background:linear-gradient(90deg,rgba(20,20,20,.85),rgba(20,20,20,.5));color:var(--white);font-family:'Raleway',Arial,sans-serif;font-size:22px;line-height:52px;padding-left:24px}
.hero-dot{top:536px;width:12px;height:12px;border-radius:50%;background:rgba(255,255,255,.92)}

/* service cards */
.service-card{top:564px;width:259px;height:240px;background:var(--white);border:1px solid var(--line);box-shadow:0 6px 8px -6px rgba(0,0,0,.25);text-align:center}
.service-photo{display:block;margin:6px 9px 0;width:239px;height:123px}
.service-title{font-family:'Raleway',Arial,sans-serif;font-weight:500;color:var(--orange);font-size:18px;margin-top:16px}
.service-text{font-size:9px;line-height:15px;color:var(--muted);margin:6px 10px 0}

/* welcome */
.welcome{left:138px;top:858px;width:528px}
.welcome h1{font-family:'Raleway',Arial,sans-serif;font-weight:400;font-size:22px;color:var(--ink);letter-spacing:.2px}
.welcome p{font-size:8.8px;line-height:15.2px;color:var(--text);margin-top:8px}
.welcome .lead{font-size:10.2px;color:var(--ink)}
.hire-btn{left:136px;top:1004px;width:115px;height:34px;border-radius:3px;background:linear-gradient(#55bff0,#1f92d8);color:var(--white);font-family:'Raleway',Arial,sans-serif;font-size:12px;line-height:34px;text-align:center;text-decoration:none;box-shadow:0 2px 3px rgba(0,0,0,.2)}

/* testimonial */
.testimonial{left:692px;top:845px;width:252px;height:197px;border:1px solid var(--line);background:linear-gradient(#ffffff 55%,#e9eaeb);text-align:center}
.testimonial h2{font-family:'Raleway',Arial,sans-serif;font-weight:500;color:var(--blue-dark);font-size:21px;margin-top:22px}
.testimonial blockquote{position:relative;font-style:italic;font-size:9.4px;line-height:15.3px;color:var(--text);margin:10px 26px 0}
.quote-mark{color:var(--blue);font-family:Georgia,serif;font-size:22px;font-style:normal;position:absolute;line-height:1}
.quote-open{left:-14px;top:-4px}
.quote-close{right:-4px;bottom:-12px}
.testimonial cite{display:block;font-style:normal;font-size:11.5px;color:var(--ink);margin-top:22px}

/* footer */
.site-footer{left:0;top:1088px;width:1074px;height:112px;background:linear-gradient(#e2e2e2,var(--footer) 8px)}
.footer-links{left:138px;top:1117px;font-family:'Raleway',Arial,sans-serif;font-size:13px;color:var(--ink)}
.footer-links span{margin:0 6px}
.copyright{left:138px;top:1143px;font-size:10.5px;color:var(--text)}
.social{left:862px;top:1117px;display:flex;gap:12px}
.social span{width:16px;height:16px;border-radius:50%;background:var(--blue-dark)}
</style>
</head>
<body>

<header>
  <div class="abs brand">
    <span class="brand-name">Bright Harbor Wiring</span>
    <span class="brand-sub">Electrical and Security</span>
  </div>
  <div class="abs enquiry">
    <span class="enquiry-label">For Enquiry</span>
    <span class="enquiry-phone">
      <svg width="18" height="20" viewBox="0 0 24 24" aria-hidden="true"><path fill="#ef7a4a" d="M6.6 10.8c1.4 2.8 3.8 5.1 6.6 6.6l2.2-2.2c.3-.3.7-.4 1-.2 1.1.4 2.3.6 3.6.6.6 0 1 .4 1 1V20c0 .6-.4 1-1 1C10.6 21 3 13.4 3 4c0-.6.4-1 1-1h3.5c.6 0 1 .4 1 1 0 1.3.2 2.5.6 3.6.1.3 0 .7-.2 1z"/></svg>
      555.210.4837
    </span>
  </div>
</header>

<nav class="abs main-nav">
  <a href="#" style="left:196px">HOME</a>
  <span class="nav-sep" style="left:256px"></span>
  <a href="#" style="left:331px">ABOUT US</a>
  <span class="nav-sep" style="left:406px"></span>
  <a href="#" style="left:498px">OUR SERVICES</a>
  <span class="nav-sep" style="left:590px"></span>
  <a href="#" style="left:681px">TESTIMONIALS</a>
  <span class="nav-sep" style="left:770px"></span>
  <a href="#" style="left:858px">CONTACT US</a>
</nav>

<section class="abs hero" role="img" aria-label="Photo of the company work van parked in a warehouse beside a scissor lift"></section>
<div class="abs hero-title">Home Renovation</div>
<div class="abs hero-sub">Construction &amp; Maintenance</div>
<span class="abs hero-dot" style="left:498px"></span>
<span class="abs hero-dot" style="left:515px"></span>
<span class="abs hero-dot" style="left:531px"></span>
<span class="abs hero-dot" style="left:547px"></span>

<article class="abs service-card" style="left:134px">
  <svg class="service-photo" viewBox="0 0 239 123" role="img" aria-label="Photo of an electrician on a ladder inside a renovation site">
    <defs><linearGradient id="g1" x1="0" x2="1"><stop offset="0" stop-color="#7c8a8e"/><stop offset="1" stop-color="#4e5254"/></linearGradient></defs>
    <path d="M0 0H239V112Q119.5 100 0 112Z" fill="url(#g1)"/>
  </svg>
  <h3 class="service-title">House Renovation</h3>
  <p class="service-text">ultrices Ut nisi erat fermentum vel congue id euismod in elit Fusce ultricies orci ac feugiat suscipit leo massa sodales velit et scelerisque mi tortor</p>
</article>

<article class="abs service-card" style="left:407px">
  <svg class="service-photo" viewBox="0 0 239 123" role="img" aria-label="Photo of a newly built kitchen with tiled walls">
    <defs><linearGradient id="g2" x1="0" x2="1"><stop offset="0" stop-color="#b3aea5"/><stop offset="1" stop-color="#8a8378"/></linearGradient></defs>
    <path d="M0 0H239V112Q119.5 100 0 112Z" fill="url(#g2)"/>
  </svg>
  <h3 class="service-title">Construction</h3>
  <p class="service-text">ultrices Ut nisi erat fermentum vel congue id euismod in elit Fusce ultricies orci ac feugiat suscipit leo massa sodales velit et scelerisque mi tortor</p>
</article>

<article class="abs service-card" style="left:681px">
  <svg class="service-photo" viewBox="0 0 239 123" role="img" aria-label="Photo of a technician repairing a wall-mounted switchboard">
    <defs><linearGradient id="g3" x1="0" x2="1"><stop offset="0" stop-color="#d9d6cf"/><stop offset="1" stop-color="#6c7a86"/></linearGradient></defs>
    <path d="M0 0H239V112Q119.5 100 0 112Z" fill="url(#g3)"/>
  </svg>
  <h3 class="service-title">Repair &amp; Maintenance</h3>
  <p class="service-text">ultrices Ut nisi erat fermentum vel congue id euismod in elit Fusce ultricies orci ac feugiat suscipit leo massa sodales velit et scelerisque mi tortor</p>
</article>

<section class="abs welcome">
  <h1>WELCOME TO BRIGHT HARBOR WIRING</h1>
  <p><span class="lead">Morbi eget arcu Morbi porta libero id ullamcorper nonummy nibh ligula pulvinar metus eget</span>iaculis tempus eros Curabitur vel mi sit amet magna malesuada ultrices Ut nisi erat fermentum vel congue id euismod in elit Fusce ultricies orci ac feugiat suscipit leo massa sodales velit et scelerisque mi tortor at ipsum cligula augue bibendum accumsan vestibulum ut commodo a mi Morbi ornare gravida elit</p>
  <p>In massa libero interdum nec interdum vel blandit sed nulla In ullamcorper est eget tempor cursus neque mi consectetuer mi a ultricies massa est sed nisl Class aptent taciti sociosqu ad litora torquent per conubia nostra per inceptos</p>
</section>
<a href="#" class="abs hire-btn">HIRE US NOW</a>

<aside class="abs testimonial">
  <h2>Testimonials</h2>
  <blockquote>
    <span class="quote-mark quote-open">&ldquo;</span>Congue id euismod in elit Fusce ultricies orci ac feugiat suscipit leo massa sodales velit et scelerisque mi tortor at ipsum cligula augue bibendum accumsan vestibulum ut commodo a mi Morbi ornare<span class="quote-mark quote-close">&rdquo;</span>
  </blockquote>
  <cite>By Author Name, City Location</cite>
</aside>

<footer class="abs site-footer"></footer>
<div class="abs footer-links">HOME<span>|</span>ABOUT US<span>|</span>SERVICES<span>|</span>TESTIMONIALS<span>|</span>CONTACT</div>
<div class="abs copyright">© 2015 Company Name&nbsp; All right reserved&nbsp; Term of Use</div>
<div class="abs social" aria-label="Social links">
  <span role="img" aria-label="Social link"></span>
  <span role="img" aria-label="Our social page"></span>
  <span role="img" aria-label="Social link"></span>
</div>

</body>
</html>
```